Copperfinch Menu

I want to re design my menu at our restaurant Copperfinch, the current menu and information about the restaurant is online at www.copperfinch-eatery.example, have attached the logo for Copperfinch as well as the new menu specifications

Menu design Specifications
· Rustic

· Raw

· Unpolished

· Urban

```html
<!DOCTYPE html>
<html lang="en">
<head>
<meta charset="utf-8">
<title>Copperfinch Eatery &amp; Bar — Menu</title>
<link rel="stylesheet" href="https://fonts.googleapis.com/css2?family=Bebas+Neue&family=PT+Sans:wght@400;700&display=swap">
<style>
  :root {
    --board-dark: #1f1f1f;
    --board-mid: #3a3a3a;
    --paper-light: #dcdcdc;
    --paper-mid: #cfcfcf;
    --ink: #111111;
    --rule-light: #f2f2f2;
  }
  * { margin: 0; padding: 0; box-sizing: border-box; }
  html, body { width: 927px; height: 1200px; overflow: hidden; }
  body {
    position: relative;
    background: radial-gradient(ellipse at 30% 40%, var(--board-mid) 0%, var(--board-dark) 70%);
    font-family: "PT Sans", Arial, sans-serif;
    color: var(--ink);
  }
  .board-texture {
    position: absolute; inset: 0;
    background:
      radial-gradient(ellipse at 80% 30%, rgba(255,255,255,0.07), transparent 60%),
      radial-gradient(ellipse at 15% 80%, rgba(255,255,255,0.05), transparent 55%);
  }
  .side-rule {
    position: absolute; top: 31px; width: 191px; height: 9px;
    border-top: 3px solid var(--rule-light);
    border-bottom: 2px solid var(--rule-light);
  }
  .side-rule--left { left: 24px; }
  .side-rule--right { left: 712px; }

  .paper {
    position: absolute; left: 236px; top: 0; width: 453px; height: 1200px;
    background: linear-gradient(160deg, var(--paper-light) 0%, var(--paper-mid) 55%, var(--paper-light) 100%);
  }
  .el { position: absolute; left: 292px; width: 342px; }

  .double-rule {
    height: 8px;
    border-top: 3px solid var(--ink);
    border-bottom: 2px solid var(--ink);
  }
  .brand {
    top: 44px;
    font-family: "Bebas Neue", Impact, sans-serif;
    font-size: 56px; line-height: 54px;
    letter-spacing: 3px;
    text-align: center;
  }
  .tagline {
    top: 104px; font-size: 11px; text-align: center;
  }

  .section-title {
    font-family: "Bebas Neue", Impact, sans-serif;
    font-size: 27px; line-height: 24px;
    letter-spacing: 0.3px;
  }
  .plus-row {
    height: 10px; overflow: hidden; white-space: nowrap;
    font-size: 10px; line-height: 10px; letter-spacing: 3.6px;
  }
  .badge {
    position: absolute; border-radius: 50%; background: var(--ink); color: #fff;
    display: flex; align-items: center; justify-content: center;
    font-weight: 700;
  }
  .badge--sm { width: 18px; height: 18px; font-size: 7px; }
  .badge--lg { width: 23px; height: 23px; font-size: 9px; }
  .badge--one { width: 17px; height: 17px; font-size: 10px; }
  .badge--two { width: 23px; height: 23px; font-size: 13px; }

  .items { list-style: none; font-size: 10.5px; }
  .item { display: flex; align-items: flex-end; height: 14.5px; line-height: 14px; }
  .item__name { white-space: nowrap; }
  .item__leader { flex: 1; border-bottom: 1px solid var(--ink); margin: 0 1px 3px; }
  .item__price { width: 22px; text-align: left; padding-left: 1px; }
  .items--single .item__price { width: 22px; }
  .items--pair .item { width: 320px; }
  .items--pair .item__price { width: 27px; }
  .items--pair .item__price:last-child { width: 20px; }
  .items--tall .item { height: 29px; }
  .item__name--wrap { white-space: normal; line-height: 14.5px; }

  .note { font-size: 10.5px; }
  .end-block { position: absolute; left: 584px; top: 1128px; width: 50px; height: 22px; background: var(--ink); }
</style>
</head>
<body>
  <div class="board-texture" role="img" aria-label="Dark chalkboard texture"></div>
  <div class="side-rule side-rule--left"></div>
  <div class="side-rule side-rule--right"></div>

  <div class="paper"></div>

  <div class="el double-rule" style="top:29px"></div>
  <h1 class="el brand">Copperfinch</h1>
  <p class="el tagline">Eatery &amp; Bar Est 2000</p>

  <!-- Snacks -->
  <h2 class="el section-title" style="top:193px">Snacks</h2>
  <div class="el plus-row" style="top:213px">+ + + + + + + + + + + + + + + + + + + + + + + + + + + + + + + + + + + + + + + + + + + + + + + +</div>
  <ul class="el items items--single" style="top:228px">
    <li class="item"><span class="item__name">Pork Crackling</span><span class="item__leader"></span><span class="item__price">05</span></li>
    <li class="item"><span class="item__name">Venison Pasties &amp; Plum Sauce</span><span class="item__leader"></span><span class="item__price">12</span></li>
    <li class="item"><span class="item__name">Lamb, Meat Balls &amp; Pomegranate Molasses</span><span class="item__leader"></span><span class="item__price">15</span></li>
    <li class="item"><span class="item__name">Pulled Pork &amp; Apple Slaw Sliders</span><span class="item__leader"></span><span class="item__price">12</span></li>
    <li class="item"><span class="item__name">Cheese Fondue &amp; Asparagus</span><span class="item__leader"></span><span class="item__price">10</span></li>
    <li class="item"><span class="item__name">Battered Fish Fingers &amp; Tartare Sauce</span><span class="item__leader"></span><span class="item__price">09</span></li>
    <li class="item"><span class="item__name">Hand Cut Fries &amp; Tomato Sauce</span><span class="item__leader"></span><span class="item__price">07</span></li>
    <li class="item"><span class="item__name">Salmon &amp; Avocado Filled Sesame Cones</span><span class="item__leader"></span><span class="item__price">12</span></li>
    <li class="item"><span class="item__name">Parmesan, Chilli &amp; Levion Skinny Fries</span><span class="item__leader"></span><span class="item__price">07</span></li>
    <li class="item"><span class="item__name">Barbequed Chicken Tulips</span><span class="item__leader"></span><span class="item__price">14</span></li>
    <li class="item"><span class="item__name">Steamed Mussels &amp; Tomato Sala</span><span class="item__leader"></span><span class="item__price">12</span></li>
    <li class="item"><span class="item__name">Garlic Bread</span><span class="item__leader"></span><span class="item__price">06</span></li>
    <li class="item"><span class="item__name">Crispy Lentil Balls &amp; Roast Garlic Yoghurt</span><span class="item__leader"></span><span class="item__price">08</span></li>
  </ul>

  <!-- Salads & Sides -->
  <h2 class="el section-title" style="top:445px">Salads &amp; Sides</h2>
  <span class="badge badge--sm" style="left:584px;top:447px">SM</span>
  <span class="badge badge--lg" style="left:609px;top:445px">LG</span>
  <div class="el plus-row" style="top:469px">+ + + + + + + + + + + + + + + + + + + + + + + + + + + + + + + + + + + + + + + + + + + + + + + +</div>
  <ul class="el items items--pair" style="top:486px">
    <li class="item"><span class="item__name">Warmed Red Skinned Potatoes with Dill &amp; Mustard</span><span class="item__leader"></span><span class="item__price">06</span><span class="item__price">09</span></li>
    <li class="item"><span class="item__name">Tomato &amp; Mixed Beans</span><span class="item__leader"></span><span class="item__price">08</span><span class="item__price">11</span></li>
    <li class="item"><span class="item__name">Char Grilled Vegetables &amp; Halloumi</span><span class="item__leader"></span><span class="item__price">07</span><span class="item__price">10</span></li>
    <li class="item"><span class="item__name">Orzo, Broadbean &amp; Feta</span><span class="item__leader"></span><span class="item__price">07</span><span class="item__price">10</span></li>
    <li class="item"><span class="item__name">Beetroot, Spinach &amp; Goats Cheese with Maple</span><span class="item__leader"></span><span class="item__price">08</span><span class="item__price">11</span></li>
    <li class="item"><span class="item__name">Mixed Leaves &amp; Citrus Emulsion</span><span class="item__leader"></span><span class="item__price">06</span><span class="item__price">09</span></li>
    <li class="item"><span class="item__name">Steamed Broccoli &amp; Sesami Butter</span><span class="item__leader"></span><span class="item__price">06</span><span class="item__price">09</span></li>
  </ul>

  <!-- Boards -->
  <h2 class="el section-title" style="top:617px">Boards &amp; Two Sides</h2>
  <span class="badge badge--one" style="left:584px;top:620px">1</span>
  <span class="badge badge--two" style="left:609px;top:617px">2</span>
  <div class="el plus-row" style="top:641px">+ + + + + + + + + + + + + + + + + + + + + + + + + + + + + + + + + + + + + + + + + + + + + + + +</div>
  <ul class="el items items--pair" style="top:660px">
    <li class="item"><span class="item__name">Beef Wellington &amp; Red Wine Jus</span><span class="item__leader"></span><span class="item__price">36</span><span class="item__price">69</span></li>
    <li class="item"><span class="item__name">Apricot Glazed Chicken Crown</span><span class="item__leader"></span><span class="item__price">34</span><span class="item__price">65</span></li>
    <li class="item"><span class="item__name">Roas Pork Scotch &amp; Caramalised Apple Sauce</span><span class="item__leader"></span><span class="item__price">32</span><span class="item__price">60</span></li>
    <li class="item"><span class="item__name">Pan Fried Line Caught Fish &amp; Lemon Pickle</span><span class="item__leader"></span><span class="item__price">35</span><span class="item__price">67</span></li>
    <li class="item"><span class="item__name">Grilled Lamb Rack &amp; Mint Sauce</span><span class="item__leader"></span><span class="item__price">38</span><span class="item__price">72</span></li>
    <li class="item"><span class="item__name">Mixed Roast Nut Loaf &amp; Rhubarb Marmelade</span><span class="item__leader"></span><span class="item__price">28</span><span class="item__price">58</span></li>
  </ul>

  <!-- Sweets -->
  <h2 class="el section-title" style="top:777px">Sweets</h2>
  <div class="el plus-row" style="top:801px">+ + + + + + + + + + + + + + + + + + + + + + + + + + + + + + + + + + + + + + + + + + + + + + + +</div>
  <ul class="el items items--single items--tall" style="top:824px">
    <li class="item"><span class="item__name item__name--wrap">Orange Pannacotta with Earl Grey<br>&amp; Cardamom Syrup</span><span class="item__leader"></span><span class="item__price">12</span></li>
    <li class="item"><span class="item__name item__name--wrap">Chocolate Terrine, Macerated Strawberries<br>&amp; Macadamia Mascarpone</span><span class="item__leader"></span><span class="item__price">14</span></li>
    <li class="item"><span class="item__name item__name--wrap">Vanilla Bean Creme Brulee with Cranberry<br>&amp; Pistachio Biscotti</span><span class="item__leader"></span><span class="item__price">12</span></li>
    <li class="item"><span class="item__name item__name--wrap">Pavlova Roulade, Kiwifruit, Summer Berries<br>&amp; Passionfruit Cream</span><span class="item__leader"></span><span class="item__price">12</span></li>
  </ul>

  <!-- Cheese -->
  <h2 class="el section-title" style="top:969px">Cheese</h2>
  <div class="el plus-row" style="top:992px">+ + + + + + + + + + + + + + + + + + + + + + + + + + + + + + + + + + + + + + + + + + + + + + + +</div>
  <ul class="el items items--single" style="top:1009px">
    <li class="item"><span class="item__name">Riverbank Aged Cheddar</span><span class="item__leader"></span><span class="item__price">16</span></li>
    <li class="item"><span class="item__name">Hilltop Triple Brie</span><span class="item__leader"></span><span class="item__price">18</span></li>
    <li class="item"><span class="item__name">Kowhai Ridge Blue</span><span class="item__leader"></span><span class="item__price">14</span></li>
  </ul>
  <p class="el note" style="top:1068px">With Dried Fruit, Nuts, Fruit Paste &amp; Wafers</p>

  <div class="end-block"></div>
  <div class="el double-rule" style="top:1148px;height:12px"></div>
</body>
</html>
```